New Company Business Card Design

I have a new company logo and I want a new business card design. I dont know if the logo file i attached is in the correct format or quality. We are a New York City Specialty construction Firm specializing in high risk out of the box projects. I want a simple and classy business card that people will his card is as crisp as the work his company does.

Target Market(s)

Clients in the heavy construction industry in New York City

Industry/Entity Type

Construction Company

Contact Information for Business Card

Simple Classy - DIFFERENT

Font styles to use
Other font styles liked:
• Mach the logo font in some way

Colors

Designer to choose colors to be used in the design.

Requirements
Must have
• Uniqueness
Nice to have
• Nothing particular - Just different and classy - Timeless
Should not have
• Goofy Shit or Gimmicky shit

```html
<!DOCTYPE html>
<html lang="en">
<head>
<meta charset="utf-8">
<title>Korvel Associates – Business Card</title>
<link href="https://fonts.googleapis.com/css2?family=Arimo:ital,wght@0,400;0,700;1,400&display=swap" rel="stylesheet">
<style>
  :root {
    --backdrop: #e9e6e1;
    --card: #f6f6f6;
    --ink: #111111;
    --band: #0b0b0b;
    --accent: #1f9bd7;
    --accent-soft: #8cc8e8;
    --muted: #2a2a2a;
  }
  * { box-sizing: border-box; margin: 0; padding: 0; }
  html, body {
    width: 1200px; height: 780px; overflow: hidden;
    background: var(--backdrop);
    font-family: "Arimo", Arial, sans-serif;
    color: var(--ink);
  }
  .stage { position: relative; width: 1200px; height: 780px; }
  .card {
    position: absolute;
    background: linear-gradient(160deg, #ffffff 0%, var(--card) 60%, #ececec 100%);
    box-shadow: 0 2px 0 #dcdcdc, 0 4px 0 #cfcfcf, 0 10px 24px rgba(0,0,0,.18);
    overflow: hidden;
  }

  /* Front */
  .card-front { left: 70px; top: 58px; width: 380px; height: 664px; }
  .brand {
    text-align: center;
    color: var(--accent);
    font-weight: 700;
    letter-spacing: 1px;
  }
  .card-front .brand { margin-top: 96px; }
  .brand-name { display: block; font-size: 46px; line-height: 1; }
  .brand-sub { display: block; font-size: 15px; letter-spacing: 5px; margin-top: 6px; }
  .person { text-align: center; margin-top: 58px; }
  .person-name { font-size: 25px; font-weight: 700; letter-spacing: .5px; }
  .person-title { font-size: 19px; color: var(--accent); margin-top: 4px; }
  .contacts { margin: 26px 48px 0; }
  .contact-row {
    border-top: 1px solid var(--accent-soft);
    text-align: center;
    padding: 6px 0 8px;
  }
  .contact-label { font-size: 14px; font-style: italic; font-weight: 700; color: var(--accent); }
  .contact-value { font-size: 19px; margin-top: 1px; }
  .address { text-align: center; font-size: 18px; line-height: 1.3; border-top: 1px solid var(--accent-soft); padding-top: 8px; }
  .card-front .base-band {
    position: absolute; left: 0; right: 0; bottom: 0; height: 92px;
    background: var(--band);
    border-top: 4px solid var(--accent);
    display: flex; align-items: center; justify-content: center;
  }
  .web { color: #ffffff; font-size: 18px; letter-spacing: 5px; }
  .web b { color: var(--accent); font-weight: 400; }

  /* Back */
  .card-back { left: 500px; top: 200px; width: 640px; height: 366px; }
  .card-back .brand { margin-top: 78px; }
  .card-back .brand-name { font-size: 58px; }
  .card-back .brand-sub { font-size: 17px; }
  .tagline {
    text-align: center; font-size: 18px; line-height: 1.35;
    color: var(--muted); margin-top: 34px;
  }
  .card-back .base-band {
    position: absolute; left: 0; right: 0; bottom: 0; height: 42px;
    background: var(--band);
    border-top: 4px solid var(--accent);
  }
</style>
</head>
<body>
<main class="stage">
  <section class="card card-front" aria-label="Card front">
    <div class="brand">
      <span class="brand-name">KORVEL</span>
      <span class="brand-sub">ASSOCIATES, INC.</span>
    </div>
    <div class="person">
      <p class="person-name">Marcus T. Halloran</p>
      <p class="person-title">President &amp; CEO</p>
    </div>
    <div class="contacts">
      <div class="contact-row">
        <p class="contact-label">Office</p>
        <p class="contact-value">555-014-2281</p>
      </div>
      <div class="contact-row">
        <p class="contact-label">Cell</p>
        <p class="contact-value">555-019-3357</p>
      </div>
      <div class="contact-row">
        <p class="contact-label">Email</p>
        <p class="contact-value">MARCUS@KORVEL.COM</p>
      </div>
      <p class="address">118 Harbor Line Road<br>Eastport, New Jersey 07000</p>
    </div>
    <div class="base-band">
      <p class="web">www.<b>KORVEL</b>.com</p>
    </div>
  </section>

  <section class="card card-back" aria-label="Card back">
    <div class="brand">
      <span class="brand-name">KORVEL</span>
      <span class="brand-sub">ASSOCIATES, INC.</span>
    </div>
    <p class="tagline">Let Korvel find creative, cost-effective solution<br>to your most complex challenges.</p>
    <div class="base-band"></div>
  </section>
</main>
</body>
</html>
```